Rtvlegal.com needs a wedsite. Law Office of Bernard T. Whitfield

Bernard T. Whitfield is a criminal law firm that is 5 years old. We have already had all the content written and now just need the website designed. We also just finished our logo design using Pixel Harbor and would like it used in the design of the website.

Industry/Entity Type

Law Firm

Number of Pages Required

5+ page

Requirements
Must have
• I was our new logo to be on the website also. I want Dallas sites as the stock pictures for the website. For example the Grey Stone Hall. I also need to be able to add ClipNest videos. It has to adjust to be seen on computers and also cell phones. I need to be able to have a information sheet for clients to fill out and submit back to me.

```html
<!DOCTYPE html>
<html lang="en">
<head>
<meta charset="utf-8">
<title>Law Office of Bernard T. Whitfield</title>
<link href="https://fonts.googleapis.com/css2?family=Lato:wght@300;400;700&display=swap" rel="stylesheet">
<style>
:root{
  --navy:#0d2a63;
  --navy-soft:#1d3b78;
  --ink:#222;
  --muted:#777;
  --line:#cfcfcf;
  --footer:#1f1f1f;
  --footer-text:#d8d8d8;
  --white:#fff;
}
*{box-sizing:border-box;margin:0;padding:0}
html,body{width:675px;height:1200px;overflow:hidden;background:var(--white)}
body{font-family:'Lato',sans-serif;color:var(--ink);position:relative}
section,header,footer{position:absolute;left:0;width:675px}
.abs{position:absolute}

/* header */
.site-header{top:0;height:52px;z-index:3}
.header-top{position:absolute;top:0;left:0;width:675px;height:23px;background:rgba(255,255,255,.85)}
.nav-band{position:absolute;top:23px;left:0;width:675px;height:29px;background:var(--white);border-top:2px solid var(--line);border-bottom:2px solid var(--line)}
.brand{position:absolute;left:103px;top:6px;display:flex;align-items:center;gap:7px}
.brand-mark{width:40px;height:40px;border-radius:50%;background:var(--navy);border:3px solid var(--white);box-shadow:0 0 0 1px var(--line)}
.brand-name{font-weight:700;font-size:11px;color:var(--navy)}
.main-nav{position:absolute;right:103px;top:0;height:25px;display:flex;font-size:6.6px;color:var(--ink)}
.main-nav a{display:flex;align-items:center;padding:0 9px;color:inherit;text-decoration:none}
.main-nav a.active{background:var(--navy);color:var(--white)}

/* hero */
.hero{top:0;height:369px;background:linear-gradient(180deg,#e9ecef 0%,#d4b3a2 30%,#b86a4e 60%,#8e4a36 100%)}
.hero-figure{position:absolute;left:395px;top:82px;width:170px;height:287px;background:linear-gradient(180deg,#3a3a3e,#141416)}
.hero-title{position:absolute;left:103px;top:165px;font-size:29px;font-weight:400;color:#111}
.hero-text{position:absolute;left:103px;top:206px;width:232px;font-size:6.4px;line-height:1.55;font-weight:700;color:#111}
.btn{display:inline-block;background:var(--navy);color:var(--white);font-size:6.6px;font-weight:700;letter-spacing:.2px;text-align:center;border-radius:2px;width:68px;height:19px;line-height:19px}
.hero .btn{position:absolute;left:103px;top:246px}

/* section titles */
.section-title{position:absolute;left:0;width:675px;text-align:center;font-size:16px;color:var(--navy);font-weight:400}
.section-sub{position:absolute;left:0;width:675px;text-align:center;font-size:6.2px;color:var(--muted)}

/* attorney */
.attorney{top:369px;height:192px}
.attorney-photo{position:absolute;left:103px;top:58px;width:188px;height:113px;background:linear-gradient(135deg,#7b6a55,#3c332a 60%,#b9a68a)}
.attorney-body{position:absolute;left:303px;top:57px;width:269px}
.attorney-body h3{font-size:9px;font-weight:400;color:#111;margin-bottom:8px}
.attorney-body p{font-size:5.4px;line-height:1.6;text-align:justify;margin-bottom:7px;color:#111}
.attorney .btn{position:absolute;left:303px;top:152px}

/* services */
.services{top:561px;height:238px;background:linear-gradient(180deg,#e4ebf5,#d3dcea 50%,#e7ecf3)}
.col-head{position:absolute;width:228px;text-align:center;font-size:9.5px;color:var(--navy)}
.col-rule{position:absolute;width:40px;height:1px;background:var(--navy)}
.col-rule::after{content:"";position:absolute;left:17px;top:-2px;width:5px;height:5px;border-radius:50%;background:var(--navy)}
.acc{position:absolute;width:228px;height:18px;border-radius:9px;border:1px solid #555;background:rgba(255,255,255,.35);font-size:6.4px;color:#444;padding-left:8px;line-height:16px}
.acc.open{border-color:var(--navy);color:var(--navy);background:rgba(255,255,255,.6)}
.acc .toggle{position:absolute;right:1px;top:1px;width:14px;height:14px;border-radius:50%;background:#444;color:var(--white);font-size:10px;line-height:13px;text-align:center}
.acc.open .toggle{background:var(--navy)}
.acc-body{position:absolute;width:218px;font-size:5.4px;line-height:1.6;color:#222}
.read-more{position:absolute;font-size:6.2px;font-weight:700;color:var(--navy)}

/* team */
.team{top:799px;height:191px}
.member{position:absolute;top:70px;width:150px;text-align:center}
.member .photo{width:80px;height:80px;border-radius:50%;margin:0 auto;border:1px solid var(--line);padding:3px;background:var(--white)}
.member .photo span{display:block;width:100%;height:100%;border-radius:50%;background:linear-gradient(180deg,#d9d3cc,#7d6e62)}
.member p{margin-top:12px;font-size:10px;color:#555}

/* footer */
.site-footer{top:990px;height:210px;background:var(--footer);color:var(--footer-text)}
.foot-head{position:absolute;top:23px;font-size:10px;color:var(--white)}
.contact-row,.social-row{position:absolute;display:flex;align-items:center;gap:8px;font-size:6.2px;line-height:1.55}
.icon{width:21px;height:21px;border-radius:50%;border:1px solid #bbb;display:flex;align-items:center;justify-content:center;flex:none}
.service-list{position:absolute;top:57px;list-style:none;font-size:5.6px}
.service-list li{height:16.5px}
.service-list b{display:inline-block;width:12px;font-weight:400}
.foot-rule{position:absolute;left:103px;top:167px;width:469px;height:1px;background:#3a3a3a}
.copyright{position:absolute;left:0;top:184px;width:675px;text-align:center;font-size:5.6px;color:var(--white)}
</style>
</head>
<body>

<section class="hero">
  <div class="hero-figure" role="img" aria-label="Attorney in a dark suit standing in front of a red stone courthouse"></div>
  <h1 class="hero-title">The Best&nbsp; Lawyers</h1>
  <p class="hero-text">Typi non habent claritatem insitam, est usus legentis in iis qui facit eorum claritatem. Investigationes demonstraverunt lectores legere me lius quod ii legunt saepius</p>
  <span class="btn">LEARN MORE</span>
</section>

<header class="site-header">
  <div class="header-top"></div>
  <div class="nav-band">
    <nav class="main-nav">
      <a class="active">Home</a><a>Attornet Profile</a><a>History</a><a>How We Can Help</a><a>Service</a><a>Contact Us</a>
    </nav>
  </div>
  <div class="brand"><span class="brand-mark"></span><span class="brand-name">Rtvlegal.com</span></div>
</header>

<section class="attorney">
  <h2 class="section-title" style="top:18px">Attorney Profile</h2>
  <p class="section-sub" style="top:39px">Lorem ipsum dolor sit amet, consectetuer</p>
  <div class="attorney-photo" role="img" aria-label="Barristers in robes presenting a case in a courtroom"></div>
  <div class="attorney-body">
    <h3>Our Aggressive Criminal Defense Team Fights for You</h3>
    <p>You are innocent unless proven guilty. But our criminal justice system often unjustly denies this fundamental constitutional right. The Law Office of Bernard T. Whitfield seeks to balance the scales of justice.</p>
    <p>Our Dallas-Fort Worth law firm solely handles criminal defense cases so we can dedicate our full resources to the pursuit of justice. Our criminal defense attorneys presume that every case we take will go to trial and aggressively advocate for you from the moment we take your case. Because the wheels of justice spin 24 hours, so do we. If you are arrested after-hours, on weekends or on holidays, we are available to handle your jail release.</p>
  </div>
  <span class="btn">LEARN MORE</span>
</section>

<section class="services" role="img" aria-label="Faint statue of Lady Justice behind the services content">
  <h2 class="section-title" style="top:22px">Our Services</h2>
  <p class="section-sub" style="top:43px">Lorem ipsum dolor sit amet, consectetuer</p>

  <h3 class="col-head" style="left:103px;top:63px">Murder and Other Homicide Offenses</h3>
  <span class="col-rule" style="left:197px;top:79px"></span>
  <div class="acc open" style="left:103px;top:89px">Our Dallas Attorneys Protect Your Rights to Justice<span class="toggle">-</span></div>
  <p class="acc-body" style="left:111px;top:111px">You have the right to remain silent and to have an attorney present for questioning. You should exercise these constitutional rights when charged with a serious crime. Do not say anything since even a seemingly innocent statement could lead</p>
  <span class="read-more" style="left:111px;top:142px">READ MORE &#10230;</span>
  <div class="acc" style="left:103px;top:157px">Homicide Defense Tactics<span class="toggle">+</span></div>
  <div class="acc" style="left:103px;top:178px">Vehicular Manslaughter Charges<span class="toggle">+</span></div>
  <div class="acc" style="left:103px;top:199px">Consult with Our Knowledgeable Criminal Defense Team 24-7<span class="toggle">+</span></div>

  <h3 class="col-head" style="left:344px;top:63px">Expungements &amp; Non-Disclosures</h3>
  <span class="col-rule" style="left:438px;top:79px"></span>
  <div class="acc open" style="left:344px;top:89px">Our Dallas Lawyers Help You Erase Your Criminal Records<span class="toggle">-</span></div>
  <p class="acc-body" style="left:352px;top:111px">A criminal record can continue to affect your life long after your arrest. Today's technology allows the public to find your criminal history online with a few simple clicks of a button and a small fee. The Internet exposes your mistake to every neigh-</p>
  <span class="read-more" style="left:352px;top:142px">READ MORE &#10230;</span>
  <div class="acc" style="left:344px;top:157px">Which Remedy Applies?<span class="toggle">+</span></div>
  <div class="acc" style="left:344px;top:178px">Are You Eligible for Record Non-Disclosure?<span class="toggle">+</span></div>
  <div class="acc" style="left:344px;top:199px">Make a Fresh Start<span class="toggle">+</span></div>
</section>

<section class="team">
  <h2 class="section-title" style="top:18px">Meet Our Criminal Defence Team</h2>
  <p class="section-sub" style="top:39px">Lorem ipsum dolor sit amet, consectetuer</p>
  <div class="member" style="left:102px"><div class="photo"><span role="img" aria-label="Portrait of Bernard T. Whitfield"></span></div><p>Bernard T. Whitfield</p></div>
  <div class="member" style="left:263px"><div class="photo"><span role="img" aria-label="Portrait of Maren Ashcombe-Lutz"></span></div><p>Maren Ashcombe-Lutz</p></div>
  <div class="member" style="left:424px"><div class="photo"><span role="img" aria-label="Portrait of Dorian Kettleway"></span></div><p>Dorian Kettleway</p></div>
</section>

<footer class="site-footer">
  <h4 class="foot-head" style="left:103px">Contact Us</h4>
  <div class="contact-row" style="left:103px;top:48px">
    <span class="icon"><svg width="9" height="9" viewBox="0 0 10 10"><path d="M5 0.5a3.2 3.2 0 0 0-3.2 3.2C1.8 6 5 9.5 5 9.5S8.2 6 8.2 3.7A3.2 3.2 0 0 0 5 .5zm0 4.4a1.2 1.2 0 1 1 0-2.4 1.2 1.2 0 0 1 0 2.4z" fill="#fff"/></svg></span>
    <span>418 Wrenfield Row<br>Marlow Bay</span>
  </div>
  <div class="contact-row" style="left:103px;top:81px">
    <span class="icon"><svg width="9" height="9" viewBox="0 0 10 10"><path d="M2.2 .8l1.6 1.9-.9 1.2a6 6 0 0 0 3.2 3.2l1.2-.9 1.9 1.6-.9 1.4C5 9.2.8 5 .8 1.7z" fill="#fff"/></svg></span>
    <span>+00 321 4455 10<br>+00 321 4455 20</span>
  </div>
  <div class="contact-row" style="left:103px;top:114px">
    <span class="icon"><svg width="9" height="9" viewBox="0 0 10 10"><rect x="1" y="2.2" width="8" height="5.6" fill="none" stroke="#fff" stroke-width="1"/><path d="M1 2.4l4 3 4-3" fill="none" stroke="#fff" stroke-width="1"/></svg></span>
    <span>office@rtvlegal.com<br>bernard@rtvlegal.com</span>
  </div>

  <h4 class="foot-head" style="left:224px">Our Service</h4>
  <ol class="service-list" style="left:224px">
    <li><b>1.</b>Attorney Profile</li><li><b>2.</b>How We Can Help</li><li><b>3.</b>Murder &amp; Other Homicide Offenses</li><li><b>4.</b>Sexual Offenses</li><li><b>5.</b>Expungements &amp; Non-Disclosures</li>
  </ol>
  <ol class="service-list" style="left:345px">
    <li><b>6.</b>Early Probation Release</li><li><b>7.</b>Probation Violations</li><li><b>8.</b>Other Violent Offenses</li><li><b>9.</b>DWI, DUI</li><li><b style="width:14px">10.</b>Drug Offenses</li>
  </ol>

  <h4 class="foot-head" style="left:465px">Follow Us</h4>
  <div class="social-row" style="left:465px;top:49px"><span class="icon"></span><span>www.chatterloop.com</span></div>
  <div class="social-row" style="left:465px;top:79px"><span class="icon"></span><span>www.quipstream.com</span></div>
  <div class="social-row" style="left:465px;top:109px"><span class="icon"></span><span>www.proflink.com</span></div>

  <div class="foot-rule"></div>
  <p class="copyright">&copy; Copyright 2015 Rtvlegal.com&nbsp; All Rights Reserved.</p>
</footer>

</body>
</html>
```